Brightmeadow Charity Ball Poster

We are looking for a poster for our upcoming event, "Brightmeadow Charity Ball" - a sit down dinner formal event hosted by our university club, OKRU.
Usually we source designs internally from our committee (even if they aren't the most amazing quality), however this time round we have no one available to do it as everyone is a volunteer.
The event's theme is 'winter wonderland', based around the snowy forests you see in Velmoria or Crown of Ashes (neither of these specific things are the theme however). Our venue is a clear-roof marque in a space surrounded by very tall pine trees giving off the forest vibe, and there are festoons strung between the trees so this is an element of warm light amongst the forest, perhaps a building or village tucked away in the forest.
The poster is for printing out at A3 size, and we will also need to create a Chatterbook event cover photo and other marketing graphics from the original poster files so some flexibility in the design and original files are required.
Things that need to be included on the poster :
---Event details
Brightmeadow Charity Ball
Saturday 12th August
7pm – midnight
Harrowgate Auditorium, KPT
Tables of 10
Members - $140
Non members - $150
All profits donated to Stride for Hope
---- Extra info and images (can be at the bottom, in corners etc,)
18+ ID required | Drink Responsibly
OKRU Logo
KPT Guild Logo
(these logos may be changed to black and white if need be)
Example images of styles, colours and the sort of landscape we want for the poster can be found in the document attached.

```html
<!DOCTYPE html>
<html lang="en">
<head>
<meta charset="utf-8">
<title>Brightmeadow Charity Ball</title>
<link rel="stylesheet" href="https://fonts.googleapis.com/css2?family=Yellowtail&family=Delius&display=swap">
<style>
  :root {
    --night-top: #4f6f7c;
    --night-mid: #2f4c58;
    --night-deep: #1c3440;
    --forest-far: #2e5a5c;
    --forest-near: #173336;
    --lime: #d6ea8c;
    --lime-text: #e4f2a6;
    --ink: #1d2f30;
    --snow: #ffffff;
  }
  * { margin: 0; padding: 0; box-sizing: border-box; }
  html, body { width: 849px; height: 1200px; overflow: hidden; }
  body { font-family: "Delius", sans-serif; background: var(--night-deep); }
  .poster {
    position: relative; width: 849px; height: 1200px; overflow: hidden;
    background:
      radial-gradient(circle at 50% 28%, rgba(255,255,255,0.45) 0, rgba(255,255,255,0.12) 120px, rgba(255,255,255,0) 300px),
      linear-gradient(180deg, var(--night-top) 0%, var(--night-mid) 45%, var(--night-deep) 100%);
    color: var(--snow); text-align: center;
  }
  .night-sky {
    position: absolute; inset: 0 0 auto 0; height: 820px;
    background:
      radial-gradient(circle at 15% 12%, rgba(255,255,255,0.12) 0, rgba(255,255,255,0) 90px),
      radial-gradient(circle at 88% 18%, rgba(255,255,255,0.10) 0, rgba(255,255,255,0) 110px),
      radial-gradient(circle at 80% 55%, rgba(255,255,255,0.08) 0, rgba(255,255,255,0) 120px),
      radial-gradient(circle at 10% 60%, rgba(255,255,255,0.08) 0, rgba(255,255,255,0) 120px);
  }
  .title {
    position: absolute; top: 70px; left: 0; right: 0;
    font-family: "Yellowtail", cursive; font-weight: 400;
    font-size: 118px; line-height: 128px; color: var(--snow);
    transform: rotate(-4deg);
  }
  .title .line-one { display: block; margin-right: 40px; }
  .title .line-two { display: block; margin-left: 60px; }
  .rule { position: absolute; left: 127px; width: 595px; height: 4px; background: var(--lime); }
  .rule.top { top: 392px; }
  .rule.bottom { top: 517px; }
  .event-details {
    position: absolute; top: 410px; left: 0; right: 0;
    color: var(--lime-text); font-size: 33px; line-height: 48px;
  }
  .pricing { position: absolute; top: 592px; left: 0; right: 0; color: var(--lime-text); }
  .pricing .tables { font-size: 30px; line-height: 44px; }
  .pricing .rates { font-size: 25px; line-height: 36px; }
  .donation-banner { position: absolute; top: 722px; left: 110px; width: 629px; height: 90px; }
  .donation-banner p {
    position: absolute; inset: 0; display: flex; align-items: center; justify-content: center;
    color: var(--ink); font-size: 32px;
  }
  .pine-forest {
    position: absolute; left: 0; right: 0; top: 820px; bottom: 0;
    background: linear-gradient(180deg, rgba(46,90,92,0) 0%, var(--forest-far) 22%, var(--forest-near) 70%, #10262a 100%);
  }
  .small-print {
    position: absolute; top: 1060px; left: 0; right: 0;
    font-size: 18px; color: var(--snow);
  }
  .partners {
    position: absolute; top: 1108px; left: 0; right: 0;
    display: flex; justify-content: center; align-items: center; gap: 60px;
  }
  .partner { display: flex; align-items: center; gap: 10px; font-size: 30px; color: var(--snow); }
  .partner .dot { width: 22px; height: 22px; border-radius: 50%; background: var(--snow); }
  .partner .square { width: 22px; height: 22px; background: var(--snow); }
</style>
</head>
<body>
<main class="poster">
  <div class="night-sky" role="img" aria-label="Snowy night sky with drifting snowflakes and soft glowing lights"></div>

  <h1 class="title"><span class="line-one">Brightmeadow</span><span class="line-two">Charity Ball</span></h1>

  <div class="rule top"></div>
  <div class="event-details">
    <p>Saturday 12th August | 7pm – midnight</p>
    <p>Harrowgate Auditorium, KPT</p>
  </div>
  <div class="rule bottom"></div>

  <div class="pricing">
    <p class="tables">Tables of 10</p>
    <p class="rates">Members - $140 | Non Members - $150</p>
  </div>

  <div class="pine-forest" role="img" aria-label="Silhouetted snowy pine forest at night"></div>

  <div class="donation-banner">
    <svg width="629" height="90" viewBox="0 0 629 90" aria-hidden="true">
      <polygon points="0,0 629,0 605,45 629,90 0,90 24,45" fill="var(--lime)"/>
    </svg>
    <p>All profits donated to Stride for Hope</p>
  </div>

  <p class="small-print">18+ ID required | Drink Responsibly</p>

  <div class="partners">
    <div class="partner"><span class="dot"></span>OKRU</div>
    <div class="partner"><span class="square"></span>KPT Guild</div>
  </div>
</main>
</body>
</html>
```